Realtor / Real Estate Lead Generation site

Need a website design for lead generation. This website connects realtors with buyers and sellers of homes. some sites i like are: quillmarsh.com, vanbridle.com, plumvestor.com. Those sites look nice and have the same purpose as mine. The name of my site is NestBridgeHub. Basically I connect people with Top producing real estate agents
Updates

Project Deadline Extended Reason: Im still waiting on all my friends to pick the design. I have sent them the link to view and comment. I will be committing payment as well. Added Monday, February 15, 2016

Target Market(s)

people looking to buy or sell a home

Industry/Entity Type

Real Estate

Coding

Coded - Design and coding required

Number of Pages Required

5+ page

Font styles to use
Sans Serif

Requirements
Must have
• 2 versions of a lead capture form. One for buyers and one for sellers. goto www.plumvestor.com and select "buyer", you will see a for asking for Price Range, Type of Home, and City or Zipcode. If you select seller it has a differnt set of questions. I like the way they have trust builders on the right hand side such as realtors faces and comments about the realtors.I would like trust builders above the fold as well, so when its viewed on a phone or computer they can see them without scrolling, something such as #1 company, please see quillmarsh-mobile.png file attached. I also have an explainer video that I would like a link to on the homepage above the fold without scrolling. please see brindlow.png file to see an example. I will upload video later. There should be a thank you page, privacy policy, terms and conditions. For ALL content see. www.789dwellmatch.com which is my current site.
• I would like the page to be mobile responsive/wordpress. Lastly, please see the form on 789dwellmatch.com. once you select the city, zipcode or address, and click "find my perfect agent, a form will come up with several different sets of questions. I would like that exact form used as I already paid for it on my other site. Thank you

```html
<!DOCTYPE html>
<html lang="en">
<head>
<meta charset="utf-8">
<title>NestBridgeHub – Find the best real estate buyer</title>
<link href="https://fonts.googleapis.com/css2?family=Fira+Sans:wght@400;500;600&family=Arimo:wght@400;700&display=swap" rel="stylesheet">
<style>
:root{
  --blue:#1b93d4;
  --blue-dark:#1582bf;
  --heading-blue:#1a8ccb;
  --orange:#d8650f;
  --orange-dark:#b04a04;
  --ink:#2b2f33;
  --muted:#6b6f73;
  --light:#f4f5f6;
  --night:#222c36;
  --footer:#151b21;
  --footer-bar:#0e1216;
  --white:#ffffff;
}
*{box-sizing:border-box;margin:0;padding:0}
html,body{width:1200px;height:2601px;overflow:hidden}
body{position:relative;font-family:"Arimo",Arial,sans-serif;color:var(--ink);background:var(--white)}
.abs{position:absolute}
.heading{font-family:"Fira Sans",Arial,sans-serif}

/* header */
.site-header{left:0;top:0;width:1200px;height:80px;background:rgba(255,255,255,.82);z-index:3}
.brand{display:flex;align-items:center;gap:8px;font-family:"Fira Sans",sans-serif;font-size:19px;color:#26323d;white-space:nowrap}
.brand-mark{width:14px;height:14px;background:var(--heading-blue)}
.site-header .brand{position:absolute;left:113px;top:30px}
.nav-link{position:absolute;top:33px;width:100px;margin-left:-50px;text-align:center;font-family:"Fira Sans",sans-serif;font-size:11.5px;letter-spacing:.3px;color:#3b4148;white-space:nowrap}
.btn-signin{position:absolute;left:988px;top:19px;width:100px;height:42px;border-radius:3px;background:linear-gradient(var(--orange),var(--orange-dark));color:#fff;font-family:"Fira Sans",sans-serif;font-size:12px;display:flex;align-items:center;justify-content:center}

/* hero */
.hero-photo{left:0;top:0;width:1200px;height:557px;background:linear-gradient(100deg,#dcdfe2 0%,#f3f4f5 35%,#e6e8ea 60%,#cfd3d6 100%)}
.hero-arrow{width:30px;height:30px;border-radius:50%;background:rgba(120,120,120,.55);top:304px}
.hero-panel{left:142px;top:262px;width:916px;height:269px;background:rgba(255,255,255,.9);box-shadow:0 0 6px rgba(0,0,0,.12);text-align:center}
.hero-title{margin-top:32px;font-size:29px;letter-spacing:.6px;color:#2c3238;font-weight:400}
.hero-sub{margin-top:10px;font-size:13px;color:#4b4f53}
.hero-tabs{margin-top:16px;display:flex;justify-content:center;gap:26px;font-family:"Fira Sans",sans-serif;font-size:18px}
.tab-active{color:var(--heading-blue);border-bottom:3px solid var(--heading-blue);padding-bottom:6px}
.tab{color:#3a3f44}
.hero-input{left:89px;top:175px;width:537px;height:57px;border:1px solid #dcdcdc;background:#fff;border-radius:3px;font-size:11px;color:#9a9ea2;text-align:left;padding:20px 24px}
.btn-find{left:647px;top:175px;width:180px;height:57px;border-radius:3px;background:linear-gradient(var(--orange),var(--orange-dark));color:#fff;font-family:"Fira Sans",sans-serif;font-size:18px;display:flex;align-items:center;justify-content:center;letter-spacing:.4px}

/* features */
.feature{width:300px;text-align:center;top:612px}
.feature-art{width:80px;height:72px;margin:0 auto;border-radius:6px}
.feature h3{margin-top:28px;font-size:18px;font-weight:500;color:var(--heading-blue);letter-spacing:.4px}
.feature p{margin-top:14px;font-size:11.5px;line-height:26px;color:#5b5f63}

/* why band */
.why-blue{left:0;top:865px;width:754px;height:434px;background:linear-gradient(120deg,var(--blue) 0%,#1f8fcf 60%,var(--blue-dark) 100%)}
.why-photo{left:754px;top:865px;width:446px;height:434px;background:linear-gradient(160deg,#e8edf1 0%,#b9c4cc 45%,#8e9ba6 100%)}
.why-kicker{left:111px;top:942px;font-size:14px;color:#fff;letter-spacing:.3px}
.why-title{left:111px;top:980px;font-size:40px;color:#fff;font-weight:400;letter-spacing:.6px;white-space:nowrap}
.why-text{left:111px;top:1044px;width:620px;font-size:11.5px;line-height:31px;color:#eaf5fc}
.btn-learn{left:111px;top:1181px;width:154px;height:52px;border-radius:3px;background:linear-gradient(#ffffff,#e3e6e8);color:var(--heading-blue);font-family:"Fira Sans",sans-serif;font-size:14px;display:flex;align-items:center;justify-content:center;letter-spacing:.4px}

/* benefits */
.benefits{left:0;top:1299px;width:1200px;height:392px;background:var(--light)}
.agent-photo{left:0;top:1299px;width:338px;height:392px;background:linear-gradient(90deg,#e7e9ea 0%,#f2f3f3 45%,#c9cdd0 100%)}
.benefit-icon{width:84px;height:84px;border-radius:50%;background:linear-gradient(var(--orange),var(--orange-dark))}
.benefit-title{left:468px;font-size:19px;font-weight:500;color:var(--heading-blue);letter-spacing:.3px}
.benefit-text{left:468px;width:620px;font-size:11.5px;line-height:25px;color:#5b5f63}
.benefit-rule{left:468px;top:1465px;width:620px;height:1px;background:#e0e2e4}

/* testimonials */
.testimonials{left:0;top:1691px;width:1200px;height:428px;background:linear-gradient(180deg,#34404c 0%,var(--night) 100%)}
.lead-form{left:111px;top:1613px;width:976px;height:163px;background:var(--blue)}
.lead-form h2{position:absolute;left:0;top:27px;width:100%;text-align:center;font-size:29px;font-weight:400;color:#fff;letter-spacing:.5px}
.field{top:81px;width:239px;height:47px;background:#fff;border-radius:2px;font-size:11px;color:#8c9094;padding:17px 12px}
.btn-submit{left:808px;top:79px;width:132px;height:51px;border-radius:3px;background:linear-gradient(var(--orange),var(--orange-dark));color:#fff;font-family:"Fira Sans",sans-serif;font-size:18px;display:flex;align-items:center;justify-content:center;letter-spacing:.5px}
.quote-title{left:0;top:1824px;width:1200px;text-align:center;font-size:25px;color:#fff;font-weight:400;letter-spacing:.4px}
.quote-text{left:160px;top:1896px;width:880px;text-align:center;font-size:12px;line-height:27px;color:#d8dde2}
.quote-author{left:0;top:1963px;width:1200px;display:flex;justify-content:center;align-items:center;gap:14px;font-size:15px;color:#fff}
.avatar{width:56px;height:56px;border-radius:50%;border:2px solid #fff;background:linear-gradient(#c9b8a8,#7b6a5c)}
.dots{left:566px;top:2070px;display:flex;gap:8px}
.dots span{width:8px;height:8px;border-radius:50%;background:#6d7781}
.dots .on{background:#fff}

/* partners */
.partner{top:2190px;display:flex;align-items:center;gap:8px;font-size:19px;color:#6f7376;transform:translateX(-50%);white-space:nowrap}
.partner i{display:block;width:18px;height:18px;background:#9ca0a3}

/* footer */
.site-footer{left:0;top:2294px;width:1200px;height:220px;background:var(--footer)}
.footer-bar{left:0;top:2514px;width:1200px;height:87px;background:var(--footer-bar);text-align:center;padding-top:37px;font-size:12px;color:#c9ced3}
.footer-bar a{color:var(--orange);text-decoration:none}
.site-footer .brand{position:absolute;left:113px;top:68px;color:#e9ecef}
.footer-about{left:113px;top:104px;width:300px;font-size:11.5px;line-height:25px;color:#c9ced3}
.footer-rule{top:54px;width:1px;height:150px;background:#2b333b}
.footer-col h4{font-family:"Fira Sans",sans-serif;font-size:13px;font-weight:500;color:#fff;letter-spacing:.4px;margin-bottom:10px}
.footer-col li{list-style:none;font-size:11.5px;color:#c9ced3;line-height:31px}
.footer-col li::before{content:"›";margin-right:8px;color:#8b939b}
.contact-line{font-size:11.5px;line-height:22px;color:#c9ced3;white-space:nowrap}
.social{top:2450px;left:884px;display:flex;gap:6px}
.social span{width:25px;height:25px;border-radius:50%;background:#8a9096}
</style>
</head>
<body>

<!-- hero -->
<div class="abs hero-photo" role="img" aria-label="Bright white interior with a staircase and tall windows"></div>

<header class="abs site-header">
  <div class="brand"><span class="brand-mark"></span>NestBridgeHub</div>
  <nav>
    <span class="nav-link" style="left:564px">FOR SELLERS</span>
    <span class="nav-link" style="left:669px">FOR BUYERS</span>
    <span class="nav-link" style="left:760px">ABOUT</span>
    <span class="nav-link" style="left:839px">SIGN UP</span>
    <span class="nav-link" style="left:933px">CONTACT US</span>
  </nav>
  <div class="btn-signin">SIGN IN</div>
</header>

<svg class="abs hero-arrow" style="left:27px" viewBox="0 0 30 30"><path d="M17 9l-6 6 6 6" fill="none" stroke="#fff" stroke-width="2"/></svg>
<svg class="abs hero-arrow" style="left:1143px" viewBox="0 0 30 30"><path d="M13 9l6 6-6 6" fill="none" stroke="#fff" stroke-width="2"/></svg>

<section class="abs hero-panel">
  <h1 class="heading hero-title">FIND THE BEST REAL ESTATE BUYER FOR YOUR NEEDS.</h1>
  <p class="hero-sub">100% Free. No obligation.</p>
  <div class="hero-tabs"><span class="tab-active">BUYER</span><span class="tab">SELLER</span></div>
  <div class="abs hero-input">City,Zip or Address</div>
  <div class="abs btn-find">FIND NOW</div>
</section>

<!-- features -->
<div class="abs feature" style="left:119px">
  <div class="feature-art" role="img" aria-label="Illustration of a house with a sale sign" style="background:linear-gradient(#f2a477,#3aa0d8)"></div>
  <h3 class="heading">SALES EXPERIENCE</h3>
  <p>Lorem ipsum dolor sit amet, consectetur adipiscing elit. Duis vel felis venenatis, placerat nulla non, hendrerit nisi.</p>
</div>
<div class="abs feature" style="left:452px">
  <div class="feature-art" role="img" aria-label="Illustration of a house under a magnifying glass" style="background:linear-gradient(#2f4a63,#e0823e)"></div>
  <h3 class="heading">PROPERTY OFFERINGS</h3>
  <p>Suspendisse feugiat libero non diam consectetur suscipit. Fusce id sem sagittis, ultrices neque non, dictum elit. Duis vitae risus at dui suscipit.</p>
</div>
<div class="abs feature" style="left:785px">
  <div class="feature-art" role="img" aria-label="Illustration of a handshake" style="background:linear-gradient(#2a7d96,#7ec7d8)"></div>
  <h3 class="heading">PROPERTY ADVISORY</h3>
  <p>Pellentesque habitant morbi tristique senectus et netus et malesuada fames ac turpis egestas. Pellentesque auctor malesuada.</p>
</div>

<!-- why -->
<div class="abs why-blue"></div>
<div class="abs why-photo" role="img" aria-label="City skyline seen through tall office windows"></div>
<p class="abs why-kicker heading">CONNECTS REALTORS WITH BUYERS AND SELLERS OF HOMES</p>
<h2 class="abs why-title heading">WHY USE A NESTBRIDGEHUB?</h2>
<p class="abs why-text">Cras dictum, odio a volutpat varius, lacus velit tempus justo, eu tincidunt lorem leo at nisl. Sed fermentum diam feugiat, suscipit nisl sed, vestibulum lorem. Integer at ultrices elit. Quisque vitae ipsum lorem. Pellentesque habitant morbi tristique senectus et netus et malesuada fames ac turpis egestas. Vestibulum eget elit finibus, dictum nibh in, feugiat arcu. Donec congue, erat nec iaculis aliquam.</p>
<div class="abs btn-learn">LEARN MORE</div>

<!-- benefits -->
<div class="abs benefits"></div>
<div class="abs agent-photo" role="img" aria-label="Smiling real estate agent holding up house keys"></div>

<svg class="abs benefit-icon" style="left:362px;top:1350px" viewBox="0 0 84 84"><path d="M28 44l14-12 14 12M32 41v14h20V41M39 55v-8h6v8" fill="none" stroke="#fff" stroke-width="3" stroke-linejoin="round"/></svg>
<h3 class="abs benefit-title heading" style="top:1358px">BUYING AND SELLING</h3>
<p class="abs benefit-text" style="top:1385px">Cras dictum, odio a volutpat varius, lacus velit tempus justo, eu tincidunt lorem leo at nisl. Sed fermentum diam feugiat, suscipit nisl sed, vestibulum lorem. Integer at ultrices elit. Quisque vitae ipsum lorem.</p>
<div class="abs benefit-rule"></div>
<svg class="abs benefit-icon" style="left:362px;top:1486px" viewBox="0 0 84 84"><circle cx="42" cy="42" r="14" fill="none" stroke="#fff" stroke-width="3"/><path d="M42 34v8l6 4" fill="none" stroke="#fff" stroke-width="3" stroke-linecap="round"/></svg>
<h3 class="abs benefit-title heading" style="top:1494px">24/7 CUSTOMER SUPPORT</h3>
<p class="abs benefit-text" style="top:1521px">Aliquam eu lacus tellus. Cum sociis natoque penatibus et magnis dis parturient montes, nascetur ridiculus mus. Fusce sit amet mollis nibh, id vehicula ex. Pellentesque dignissim vestibulum magna.</p>

<!-- testimonials -->
<div class="abs testimonials" role="img" aria-label="Dark city skyline at dusk"></div>

<section class="abs lead-form">
  <h2 class="heading">GET FREE PERSONALISED ADVISE</h2>
  <div class="abs field" style="left:38px">Name</div>
  <div class="abs field" style="left:295px">Email Address</div>
  <div class="abs field" style="left:551px">Phone</div>
  <div class="abs btn-submit">SUBMIT</div>
</section>

<h2 class="abs quote-title heading">WHAT PEOPLE HAVE TO SAY</h2>
<p class="abs quote-text">Cras dictum, odio a volutpat varius, lacus velit tempus justo, eu tincidunt lorem leo at nisl. Sed fermentum diam feugiat, suscipit nisl sed, vestibulum lorem. Integer at ultrices elit. Quisque vitae ipsum lorem.</p>
<div class="abs quote-author"><div class="avatar" role="img" aria-label="Customer portrait"></div>Lena Marsh..., Location</div>
<div class="abs dots"><span></span><span></span><span class="on"></span><span></span></div>

<!-- partners -->
<div class="abs partner" style="left:168px"><i></i>Elmgrove</div>
<div class="abs partner" style="left:329px"><i></i>Brightmind</div>
<div class="abs partner" style="left:498px"><i></i>Pointwell</div>
<div class="abs partner" style="left:659px"><i></i>Sorrelwood</div>
<div class="abs partner" style="left:829px"><i></i>Beaconmere</div>
<div class="abs partner" style="left:1023px"><i></i>Kitefield</div>

<!-- footer -->
<footer class="abs site-footer">
  <div class="brand"><span class="brand-mark"></span>NestBridgeHub</div>
  <p class="abs footer-about">Lorem ipsum dolor sit amet, consectetuer adipiscing elit, sed diam nonummy nibh euismod tincidunt ut laoreet dolore magna aliquam erat volutpat.</p>
  <div class="abs footer-rule" style="left:435px"></div>
  <div class="abs footer-col" style="left:479px;top:42px"><h4>ABOUT US</h4><ul><li>Home</li><li>Login</li><li>Services</li><li>Testimonials</li></ul></div>
  <div class="abs footer-rule" style="left:626px"></div>
  <div class="abs footer-col" style="left:685px;top:42px"><h4>QUICK LINKS</h4><ul><li>Get started</li><li>FAQs</li><li>Careers</li><li>Privacy &amp; Terms</li></ul></div>
  <div class="abs footer-rule" style="left:850px"></div>
  <svg class="abs" style="left:884px;top:50px" width="18" height="26" viewBox="0 0 18 26"><path d="M9 1a8 8 0 0 0-8 8c0 6 8 16 8 16s8-10 8-16a8 8 0 0 0-8-8z" fill="var(--orange)"/><circle cx="9" cy="9" r="3" fill="var(--footer)"/></svg>
  <p class="abs contact-line" style="left:919px;top:46px">9870 St Lorem Ipsm, Lorem Ipsm,<br>Lorem Ipsm, 45 Fr 45.</p>
  <svg class="abs" style="left:884px;top:98px" width="24" height="24" viewBox="0 0 24 24"><rect width="24" height="24" rx="4" fill="var(--orange)"/><path d="M8 6l3 3-2 2c1 2 2 3 4 4l2-2 3 3-2 2c-5 0-10-5-10-10z" fill="#fff"/></svg>
  <p class="abs contact-line" style="left:919px;top:96px">Telephone: &nbsp;(555) 014 2290<br>Mail : hello@nestbridgehub.com</p>
</footer>
<div class="abs social"><span></span><span></span><span></span><span></span></div>
<div class="abs footer-bar">NestBridgeHub © 2016 • <a href="#">Sitemap</a></div>

</body>
</html>
```